Cover for new song release

Song title: “Paper Lantern”. It’s a song about being in the moment. (Verse lyrics: “You can have your eyes wide open and still not even know...For every two steps forward take Paper Lantern and take in all the beauty all around.”

```html
<!DOCTYPE html>
<html lang="en">
<head>
<meta charset="utf-8">
<title>Paper Lantern — Single Cover</title>
<link rel="stylesheet" href="https://fonts.googleapis.com/css2?family=Montserrat:wght@300&display=swap">
<style>
  :root {
    --sky-gold: #e6b873;
    --sky-orange: #f59a4a;
    --sky-coral: #ef6a52;
    --sky-rose: #d9405c;
    --sky-magenta: #a82a60;
    --sky-violet: #5e2a78;
    --sky-indigo: #34246e;
    --sky-night: #271d63;
    --art-teal: #5f8a5e;
    --art-plum: #6a2f5a;
    --art-deep: #3a1f6a;
    --art-indigo: #2a1d66;
    --title-ink: #e9dbe8;
  }
  html, body {
    margin: 0;
    padding: 0;
    width: 1200px;
    height: 1200px;
    overflow: hidden;
    background: var(--sky-night);
  }
  .cover {
    position: relative;
    width: 1200px;
    height: 1200px;
    overflow: hidden;
    background: linear-gradient(180deg,
      var(--sky-gold) 0%,
      var(--sky-orange) 22%,
      var(--sky-coral) 42%,
      var(--sky-rose) 52%,
      var(--sky-magenta) 62%,
      var(--sky-violet) 76%,
      var(--sky-indigo) 88%,
      var(--sky-night) 100%);
  }
  .sky-streaks,
  .feature-art {
    position: absolute;
    inset: 0;
    width: 1200px;
    height: 1200px;
  }
  .song-title {
    position: absolute;
    left: 0;
    width: 1170px;
    top: 683px;
    margin: 0;
    text-align: center;
    font-family: "Montserrat", "Helvetica Neue", Arial, sans-serif;
    font-weight: 300;
    font-size: 34px;
    letter-spacing: 0.95em;
    text-indent: 0.95em;
    color: var(--title-ink);
    line-height: 1;
    white-space: nowrap;
  }
</style>
</head>
<body>
  <main class="cover">
    <svg class="sky-streaks" viewBox="0 0 1200 1200" aria-hidden="true">
      <defs>
        <filter id="soft-blur"><feGaussianBlur stdDeviation="14"/></filter>
      </defs>
      <path d="M0 400 C 80 395, 170 405, 175 420 C 150 440, 100 450, 0 460 Z" fill="#f7b43c" opacity="0.75" filter="url(#soft-blur)"/>
      <path d="M0 530 C 200 560, 420 610, 640 640 L 640 680 C 420 660, 200 620, 0 600 Z" fill="#f08a48" opacity="0.45" filter="url(#soft-blur)"/>
      <path d="M700 540 C 900 560, 1050 600, 1200 630 L 1200 700 C 1050 670, 900 640, 700 620 Z" fill="#c23a6a" opacity="0.35" filter="url(#soft-blur)"/>
      <path d="M0 900 C 300 880, 700 900, 1200 880 L 1200 960 C 700 980, 300 960, 0 980 Z" fill="#3a2a7a" opacity="0.4" filter="url(#soft-blur)"/>
    </svg>

    <svg class="feature-art" viewBox="0 0 1200 1200" role="img" aria-label="Illustration area: a dreamy double-exposure figure gazing upward, filled with painted brushstrokes in teal, plum and indigo against the sunset">
      <defs>
        <linearGradient id="art-fill" x1="0" y1="0" x2="0" y2="1">
          <stop offset="0" stop-color="var(--art-teal)"/>
          <stop offset="0.32" stop-color="var(--art-plum)"/>
          <stop offset="0.66" stop-color="var(--art-deep)"/>
          <stop offset="1" stop-color="var(--art-indigo)"/>
        </linearGradient>
        <radialGradient id="art-glow" cx="0.42" cy="0.22" r="0.5">
          <stop offset="0" stop-color="#7fa46a" stop-opacity="0.45"/>
          <stop offset="1" stop-color="#7fa46a" stop-opacity="0"/>
        </radialGradient>
        <filter id="edge-soften" x="-20%" y="-20%" width="140%" height="140%">
          <feGaussianBlur stdDeviation="22"/>
        </filter>
      </defs>
      <rect class="feature-column" x="300" y="90" width="640" height="1200" rx="320" ry="320"
            fill="url(#art-fill)" opacity="0.85" filter="url(#edge-soften)"/>
      <ellipse class="feature-glow" cx="580" cy="300" rx="280" ry="240" fill="url(#art-glow)"/>
    </svg>

    <h1 class="song-title">PAPER LANTERN</h1>
  </main>
</body>
</html>
```